Landing Page for a Social Survey

Hi guys,
we need an elegant landing page for a new project. It's a social survey where users need to answer some questions to participate at a lottery.
I attached an example about what we want. As in the example the design should be very elegant and engage to user to click on the button and take part in the survey.
Also the design should look a bit like lumbrook.
If you have any questions, don't hesitate to ask. I'll try to respond as soon as possible.
Please use the following texts:
Header: "Social Network Umfrage"
Headline above the text: "Herzlichen Glückwunsch"
Text:
"Sie wurden als einer von wenigen Nutzern aus Berlin und Umgebung ausgewählt an unserer Umfrage über Social Networks teilzunehmen.
Die Beantwortung der Fragen dauert nur wenige Sekunden. Als Dankeschön für Ihre Teilnahme können Sie ein Zelvo4, Trenu2 oder Pelwin Slate gewinnen."
Button: "Jetzt teilnehmen"

```html
<!DOCTYPE html>
<html lang="de">
<head>
<meta charset="utf-8">
<title>Social Network Umfrage</title>
<link href="https://fonts.googleapis.com/css2?family=Questrial&family=Arimo:wght@400;700&display=swap" rel="stylesheet">
<style>
  :root {
    --brand-blue: #3a5a9a;
    --tab-blue: #34559a;
    --bar-blue: #2d6096;
    --top-line: #2f4f8f;
    --header-top: #e6eaf1;
    --header-bottom: #fbfcfd;
    --glow: #d3def2;
    --card-border: #cfd3d8;
    --text: #1d1d1d;
    --button-green: #5f9e45;
    --button-green-dark: #4f8a38;
    --footer-text: #8a8a8a;
    --dots: #cdd3dc;
    --gift-light: #ededed;
    --gift-warm: #e4cfb0;
  }
  * { margin: 0; padding: 0; box-sizing: border-box; }
  html, body { width: 1200px; height: 620px; overflow: hidden; background: #fff; }
  body { position: relative; font-family: "Questrial", sans-serif; color: var(--text); }

  .site-header {
    position: absolute; left: 0; top: 0; width: 1200px; height: 73px;
    border-top: 3px solid var(--top-line);
    background: linear-gradient(var(--header-top), var(--header-bottom));
    border-bottom: 1px dotted var(--dots);
  }
  .site-title {
    position: absolute; left: 136px; top: 15px;
    font-family: "Arimo", sans-serif; font-weight: 700; font-size: 31px;
    color: var(--brand-blue); letter-spacing: 0.6px;
  }
  .date-tab {
    position: absolute; left: 896px; top: 0; width: 168px; height: 31px;
    background: var(--tab-blue); border-radius: 0 0 4px 4px;
    box-shadow: 0 2px 3px rgba(0,0,0,.25);
    color: #fff; font-family: "Arimo", sans-serif; font-size: 18px;
    text-align: center; line-height: 30px;
  }

  .stage-glow {
    position: absolute; left: 0; top: 293px; width: 1200px; height: 200px;
    background: radial-gradient(ellipse 620px 170px at 600px 0, var(--glow), rgba(255,255,255,0) 100%);
  }

  .gift-placeholder {
    position: absolute; left: 330px; top: 108px; width: 113px; height: 104px;
    border-radius: 6px;
    background: linear-gradient(135deg, var(--gift-warm), var(--gift-light) 70%);
    box-shadow: 0 3px 5px rgba(0,0,0,.18);
  }

  .invite-card {
    position: absolute; left: 380px; top: 148px; width: 438px; height: 211px;
    background: linear-gradient(#fff, #f8f8f8);
    border: 1px solid var(--card-border); border-radius: 3px;
    box-shadow: 0 1px 4px rgba(0,0,0,.15);
  }
  .invite-headline {
    position: absolute; left: 8px; top: 7px; width: 418px; height: 31px;
    background: var(--bar-blue); border-radius: 4px;
    color: #fff; font-size: 21px; font-weight: 400; line-height: 31px; padding-left: 9px;
  }
  .headline-pointer { position: absolute; left: 16px; top: 38px; }
  .invite-body {
    position: absolute; left: 16px; top: 51px; width: 420px;
    font-size: 14.2px; line-height: 16px;
  }
  .invite-body p { margin-bottom: 10px; }
  .invite-body .prizes { line-height: 23px; margin-top: 14px; }
  .invite-body strong { font-weight: 700; font-family: "Arimo", sans-serif; }

  .cta-button {
    position: absolute; left: 620px; top: 338px; width: 177px; height: 45px;
    background: linear-gradient(var(--button-green), var(--button-green-dark));
    border: 2px solid #eef3ea; border-radius: 3px;
    box-shadow: 0 1px 5px rgba(0,0,0,.35);
    color: #fff; font-size: 19px; line-height: 40px; text-align: center;
    text-decoration: none;
  }

  .site-footer {
    position: absolute; left: 0; top: 563px; width: 1200px; height: 57px;
    border-top: 1px dotted var(--dots);
  }
  .copyright {
    position: absolute; left: 825px; top: 22px;
    font-family: "Arimo", sans-serif; font-size: 11px; color: var(--footer-text);
  }
</style>
</head>
<body>
  <header class="site-header">
    <h1 class="site-title">Social Network Umfrage</h1>
    <div class="date-tab">Juni, 30, 2011</div>
  </header>

  <div class="stage-glow"></div>

  <div class="gift-placeholder" role="img" aria-label="Geschenkbox mit Band und roter Schleife"></div>

  <section class="invite-card">
    <h2 class="invite-headline">Herzlichen Glückwunsch</h2>
    <svg class="headline-pointer" width="14" height="8" viewBox="0 0 14 8"><path d="M0 0 H14 L7 8 Z" fill="#2d6096"/></svg>
    <div class="invite-body">
      <p>Sie wurden als einer von wenigen Nutzern aus Berlin und Umgebung ausgewählt an unserer Umfrage über Social<br>Networks teilzunehmen.</p>
      <p>Die Beantwortung der Fragen dauert nur wenige Sekunden.</p>
      <p class="prizes">Als Dankeschön für Ihre Teilnahme können Sie ein <strong>Zelvo4</strong>,<br><strong>Trenu2</strong> oder <strong>Pelwin Slate</strong> gewinnen</p>
    </div>
  </section>

  <a class="cta-button" href="#">Jetzt teilnehmen</a>

  <footer class="site-footer">
    <p class="copyright">2011 surveyprizehub.com All rights reserved.</p>
  </footer>
</body>
</html>
```